Health and Wellness company needs flyer to promote free seminar

Stride reform studio is a health and wellness company that offers an exercise program designed by physical therapists to help relieve pain and improve mobility. Our business is a new concept that is not well understood by the public. In order to promote our business we offer a free seminar where we present information regarding the underlying cause of pain and tightness. During the seminar we also perform a posture screen and movement testing for all participants.

Target Market(s)

Mostly healthy and active women ages 25-65

Industry/Entity Type

Health And Wellness

Font styles to use
Sans Serif

Colors

Designer to choose colors to be used in the design.

Requirements
Must have
• Title: Eliminate Pain and Tightness For Good
• Paragraph: Stride Reform Studio offers a free 60 minute seminar: "The Busy Walker's Handbook to Bending and Standing Taller."
• What to Expect:
• • Identify the underlying cause of your pain and mobility issues
• • Expose what gets in the way of you moving and feeling better
• • Learn why traditional exercises don’t help and can actually make the problem worse
• • Reveal what your posture is saying and how that impacts you
• • Experience your muscle imbalances through movement tests
• • Discover the training method that realigns your posture, increases your mobility and reduces your pain
• Call to action: RSVP online at stridereformstudio.com
Nice to have
• Use a relevant image showing a female dealing with tightness in the low back, legs, etc.
• Emphasize that the seminar is FREE.
• Make the call to action prominent.

```html
<!DOCTYPE html>
<html lang="en">
<head>
<meta charset="utf-8">
<title>Stride Reform Studio – Free Seminar Flyer</title>
<link rel="stylesheet" href="https://fonts.googleapis.com/css2?family=Bebas+Neue&family=Oswald:wght@500;600&family=Quicksand:wght@600;700&family=Lato:wght@400;700&display=swap">
<style>
  :root {
    --brand-blue: #4a4fb3;
    --brand-orange: #f7931e;
    --ink: #3a3a3a;
    --muted: #555a66;
    --stage: #e4e4e4;
    --paper: #ffffff;
  }
  * { box-sizing: border-box; margin: 0; padding: 0; }
  html, body { width: 1200px; height: 1200px; overflow: hidden; background: var(--stage); }
  .flyer {
    position: absolute; left: 197px; top: 30px; width: 806px; height: 1140px;
    background: var(--paper); overflow: hidden; font-family: "Lato", sans-serif; color: var(--muted);
    box-shadow: 0 6px 24px rgba(0,0,0,.15);
  }
  .hero { position: absolute; left: 0; top: 0; width: 806px; height: 620px; }
  .brand {
    position: absolute; right: 40px; top: 108px; display: flex; align-items: center; gap: 10px;
    font-family: "Quicksand", sans-serif; font-weight: 700; font-size: 26px; color: var(--brand-blue);
  }
  .brand-mark { width: 40px; height: 40px; background: var(--brand-orange); border-radius: 4px; }
  .badge {
    position: absolute; left: 565px; top: 290px; width: 206px; height: 206px; border-radius: 50%;
    background: radial-gradient(circle at 40% 35%, #ffb04a, var(--brand-orange) 65%);
    border: 9px solid #cfcfd4; box-shadow: 0 4px 14px rgba(0,0,0,.3); z-index: 2;
    display: flex; flex-direction: column; align-items: center; justify-content: center;
    font-family: "Bebas Neue", sans-serif; color: var(--brand-blue); line-height: .9;
  }
  .badge-free { font-size: 88px; }
  .badge-seminar { font-size: 48px; }
  .inset { position: absolute; border-radius: 50%; }
  .inset-stretch { left: 410px; top: 420px; width: 165px; height: 165px; border: 6px solid var(--brand-orange);
    background: linear-gradient(160deg, #8a7a5e, #5f6b3f 60%, #c9c0ae); }
  .inset-back { left: 560px; top: 468px; width: 178px; height: 178px; border: 6px solid var(--brand-blue);
    background: linear-gradient(180deg, #8fc4e4, #d9b59a 55%, #e7a9c0); }
  .title-main {
    position: absolute; left: 40px; top: 515px; transform: rotate(4deg); transform-origin: left top;
    font-family: "Bebas Neue", sans-serif; font-size: 54px; font-weight: 400; color: var(--brand-blue);
    white-space: nowrap;
  }
  .title-sub {
    position: absolute; left: 36px; top: 572px; transform: rotate(4deg); transform-origin: left top;
    font-family: "Quicksand", sans-serif; font-weight: 700; font-size: 32px; color: var(--brand-orange);
    white-space: nowrap;
  }
  .offer { position: absolute; left: 400px; top: 668px; width: 370px; }
  .offer-lead { font-family: "Oswald", sans-serif; font-weight: 600; font-size: 23px; color: var(--ink); }
  .offer-free { font-family: "Oswald", sans-serif; font-weight: 500; font-size: 23px; color: var(--brand-orange); }
  .offer-free span { color: var(--ink); }
  .offer-guide { font-family: "Oswald", sans-serif; font-weight: 600; font-size: 24px; color: var(--ink); margin-top: 8px; }
  .offer-guide-sub { font-family: "Quicksand", sans-serif; font-weight: 700; font-size: 20px; color: var(--brand-blue); }
  .expect { position: absolute; left: 40px; top: 690px; width: 330px; }
  .expect-heading { display: flex; align-items: center; gap: 10px; font-family: "Quicksand", sans-serif;
    font-weight: 700; font-size: 15px; color: var(--brand-blue); margin-bottom: 14px; }
  .expect-heading::after { content: ""; flex: 1; height: 1px; background: #b9bccb; }
  .points { list-style: none; }
  .point { display: flex; gap: 12px; font-size: 14px; line-height: 1.3; margin-bottom: 12px; color: var(--muted); }
  .point svg { flex: none; width: 26px; height: 26px; stroke: var(--brand-blue); fill: none; stroke-width: 1.8; }
  .expect-right { left: 400px; top: 830px; width: 370px; }
  .cta {
    position: absolute; left: 56px; top: 985px; width: 694px; height: 50px; border-radius: 25px;
    background: var(--brand-orange); box-shadow: 0 4px 10px rgba(0,0,0,.2); z-index: 2;
    display: flex; align-items: center; gap: 10px; padding: 0 24px;
    font-family: "Quicksand", sans-serif; font-weight: 700; font-size: 20px; color: #fff;
  }
  .cta svg { width: 24px; height: 24px; stroke: #fff; fill: none; stroke-width: 1.8; flex: none; }
  .footer {
    position: absolute; left: 0; top: 1010px; width: 806px; height: 106px; background: var(--brand-blue);
    display: flex; align-items: center; justify-content: center; gap: 36px; padding-top: 28px;
    font-size: 14px; color: #fff;
  }
  .footer-item { display: flex; align-items: center; gap: 8px; }
  .footer-item svg { width: 16px; height: 16px; fill: #fff; }
</style>
</head>
<body>
<main class="flyer">
  <svg class="hero" viewBox="0 0 806 620">
    <defs>
      <linearGradient id="hero-scene" x1="0" y1="0" x2="0" y2="1">
        <stop offset="0" stop-color="#cfd6e6"/>
        <stop offset=".35" stop-color="#e9d6c8"/>
        <stop offset=".6" stop-color="#7f8f74"/>
        <stop offset="1" stop-color="#4d5d34"/>
      </linearGradient>
    </defs>
    <path d="M0 452 C170 540 320 525 470 495 C610 468 720 520 806 580" fill="none" stroke="var(--brand-orange)" stroke-width="22"/>
    <path d="M0 440 C170 520 320 505 470 478 C610 452 720 502 806 560" fill="none" stroke="var(--brand-blue)" stroke-width="16"/>
    <path d="M0 0 H806 V545 C720 490 610 440 470 468 C320 496 170 510 0 430 Z" fill="url(#hero-scene)"
          role="img" aria-label="Photo of a woman holding a balancing yoga pose on a mat on a misty mountain ridge"/>
  </svg>

  <div class="brand"><span class="brand-mark"></span>stridereformstudio</div>

  <div class="inset inset-stretch" role="img" aria-label="Photo of a woman stretching her back in a forest"></div>
  <div class="inset inset-back" role="img" aria-label="Photo of a woman holding her lower back in pain by the sea"></div>

  <div class="badge"><span class="badge-free">FREE</span><span class="badge-seminar">SEMINAR</span></div>

  <h1 class="title-main">TIGHTNESS FOR GOOD</h1>
  <p class="title-sub">Tightness For Good</p>

  <section class="offer">
    <p class="offer-lead">Stride Reform Studio offers a</p>
    <p class="offer-free">FREE 60 MINUTE <span>seminar</span></p>
    <p class="offer-guide">The Busy Walker's Handbook</p>
    <p class="offer-guide-sub">to Bending and Standing Taller</p>
  </section>

  <section class="expect">
    <h2 class="expect-heading">What to Expect:</h2>
    <ul class="points">
      <li class="point"><svg viewBox="0 0 24 24"><circle cx="10" cy="10" r="6"/><path d="M15 15l6 6"/></svg>Identify the underlying cause of your pain and mobility issues</li>
      <li class="point"><svg viewBox="0 0 24 24"><rect x="5" y="3" width="14" height="18" rx="1"/><path d="M8 9h8M8 13h8M8 17h5"/></svg>Expose what gets in the way of you moving and feeling better</li>
      <li class="point"><svg viewBox="0 0 24 24"><path d="M2 5h8a2 2 0 0 1 2 2v13a2 2 0 0 0-2-2H2zM22 5h-8a2 2 0 0 0-2 2v13a2 2 0 0 1 2-2h8z"/></svg>Learn why traditional exercises don't help and can actually make the problem worse</li>
    </ul>
  </section>

  <section class="expect expect-right">
    <ul class="points">
      <li class="point"><svg viewBox="0 0 24 24"><path d="M2 12s4-7 10-7 10 7 10 7-4 7-10 7S2 12 2 12z"/><circle cx="12" cy="12" r="3"/></svg>Reveal what your posture is saying and how that impacts you</li>
      <li class="point"><svg viewBox="0 0 24 24"><path d="M7 21v-4a7 7 0 1 1 10-6l2 4h-2v3h-4v3"/></svg>Experience your muscle imbalances through movement tests</li>
      <li class="point"><svg viewBox="0 0 24 24"><rect x="3" y="3" width="7" height="7"/><rect x="14" y="3" width="7" height="7"/><rect x="3" y="14" width="7" height="7"/><rect x="14" y="14" width="7" height="7"/></svg>Discover the training method that realigns your posture, increases your mobility and reduces your pain</li>
    </ul>
  </section>

  <div class="cta">
    <svg viewBox="0 0 24 24"><path d="M9 11V4a2 2 0 0 1 4 0v6l5 1a2 2 0 0 1 2 2l-1 6a3 3 0 0 1-3 3h-5l-5-6 2-2 2 2"/></svg>
    Sign up online at
    <svg viewBox="0 0 24 24"><circle cx="12" cy="12" r="9"/><path d="M3 12h18M12 3c3 3 3 15 0 18M12 3c-3 3-3 15 0 18"/></svg>
    stridereformstudio.com/free-seminar
  </div>

  <footer class="footer">
    <span class="footer-item"><svg viewBox="0 0 24 24"><path d="M12 2a7 7 0 0 0-7 7c0 5 7 13 7 13s7-8 7-13a7 7 0 0 0-7-7zm0 9.5A2.5 2.5 0 1 1 12 6.5a2.5 2.5 0 0 1 0 5z"/></svg>1480 Maple Ridge Road Austin, TX 78701</span>
    <span class="footer-item"><svg viewBox="0 0 24 24"><path d="M6.6 10.8a15 15 0 0 0 6.6 6.6l2.2-2.2a1 1 0 0 1 1-.25 11.4 11.4 0 0 0 3.6.57 1 1 0 0 1 1 1V20a1 1 0 0 1-1 1A17 17 0 0 1 3 4a1 1 0 0 1 1-1h3.5a1 1 0 0 1 1 1c0 1.25.2 2.45.57 3.57a1 1 0 0 1-.25 1z"/></svg>(555) 014-2290</span>
  </footer>
</main>
</body>
</html>
```